Business Card Design Project

Use our current logo. Clean design.

Industry/Entity Type

Business

Requirements
Must have
• Marisela DUBRANCQ
M. Law
Managing Partner

Alpenvorsa AG
Kornhalmweg 214
CH-3097 Liebefeld

M. +41 79 412 56 27
T. +41 31 928 44 10
F. +41 31 928 44 19

m.dubrancq@alpenvorsa-example.com
www.alpenvorsa-example.com

```html
<!DOCTYPE html>
<html lang="en">
<head>
<meta charset="utf-8">
<title>Alpenvorsa AG – Business Card</title>
<link rel="stylesheet" href="https://fonts.googleapis.com/css2?family=Tinos&display=swap">
<style>
  :root {
    --page-bg: #ffffff;
    --card-bg: #ffffff;
    --card-border: #3c3c3c;
    --accent-red: #e41b23;
    --charcoal: #3a3a3c;
    --text-grey: #4a4a4a;
    --rule-grey: #5a5a5a;
    --logo-white: #ffffff;
  }
  html, body {
    margin: 0;
    padding: 0;
    width: 1200px;
    height: 1000px;
    overflow: hidden;
    background: var(--page-bg);
  }
  .canvas {
    position: relative;
    width: 1200px;
    height: 1000px;
    font-family: "Tinos", "Times New Roman", serif;
  }
  .card {
    position: absolute;
    left: 346px;
    top: 81px;
    width: 501px;
    height: 819px;
    box-sizing: border-box;
    border: 1px solid var(--card-border);
    background: var(--card-bg);
    overflow: hidden;
  }
  .card__wave {
    position: absolute;
    left: 0;
    top: 0;
    width: 501px;
    height: 819px;
  }
  .edge-tab {
    position: absolute;
    top: 101px;
    width: 10px;
    height: 83px;
    background: var(--accent-red);
  }
  .edge-tab--left { left: 0; }
  .edge-tab--right { right: 0; }
  .holder__name {
    position: absolute;
    left: 0;
    width: 100%;
    top: 104px;
    margin: 0;
    text-align: center;
    font-size: 27px;
    font-weight: 400;
    color: var(--accent-red);
    line-height: 1;
  }
  .holder__rule {
    position: absolute;
    left: 58px;
    width: 391px;
    top: 146px;
    height: 2px;
    background: var(--rule-grey);
  }
  .holder__role {
    position: absolute;
    left: 0;
    width: 100%;
    top: 157px;
    margin: 0;
    text-align: center;
    font-size: 21px;
    color: var(--text-grey);
    line-height: 1;
  }
  .address {
    position: absolute;
    right: 271px;
    top: 316px;
    margin: 0;
    text-align: right;
    font-style: normal;
    font-size: 21px;
    line-height: 35px;
    color: var(--text-grey);
  }
  .contact-divider {
    position: absolute;
    left: 246px;
    top: 301px;
    width: 2px;
    height: 205px;
    background: var(--rule-grey);
  }
  .phones {
    position: absolute;
    left: 260px;
    top: 386px;
    margin: 0;
    font-size: 21px;
    line-height: 35px;
    color: var(--text-grey);
  }
  .online {
    position: absolute;
    left: 35px;
    top: 620px;
    margin: 0;
    font-size: 20px;
    line-height: 34px;
    color: var(--accent-red);
  }
  .brand-name {
    position: absolute;
    right: 26px;
    top: 768px;
    margin: 0;
    font-size: 20px;
    letter-spacing: 1px;
    color: var(--logo-white);
    line-height: 1;
  }
</style>
</head>
<body>
<div class="canvas">
  <section class="card" aria-label="Business card">
    <svg class="card__wave" viewBox="0 0 501 819" aria-hidden="true">
      <path d="M0,741 Q400,760 501,514 L501,819 L0,819 Z" fill="var(--accent-red)"/>
      <path d="M0,744 Q430,742 501,552 L501,819 L0,819 Z" fill="var(--charcoal)"/>
    </svg>

    <span class="edge-tab edge-tab--left"></span>
    <span class="edge-tab edge-tab--right"></span>

    <h1 class="holder__name">Marisela DUBRANCQ, M. Law</h1>
    <div class="holder__rule"></div>
    <p class="holder__role">Managing Partner</p>

    <address class="address">
      Alpenvorsa AG<br>
      Kornhalmweg 214<br>
      CH-3097 Liebefeld
    </address>
    <div class="contact-divider"></div>
    <p class="phones">
      M. +41 79 412 56 27<br>
      T. +41 31 928 44 10<br>
      F. +41 31 928 44 19
    </p>

    <p class="online">
      m.dubrancq@alpenvorsa-example.com<br>
      www.alpenvorsa-example.com
    </p>

    <p class="brand-name">ALPENVORSA</p>
  </section>
</div>
</body>
</html>
```